Lorvane Botanic- New and unique line of Pet Products

Hi,

Lorvane Botanic is a manufacturer of natural products.

We need fresh and creative labels, for our new pet care product line:
- Specially scented for male- dog shampoo called "Pippin"
- Specially scented for female- dog shampoo called "Velvet furry"
- Cat cleaning wipes
- Stain and odor remover (for pet urine)

For more info on the products:
Lorvanebotanic.com
(please don't rely on the current labels for the pet products)

ATTACHED- you will find 2 products from Stallmart, which we like the design, as an example.

Best wishes,
Oren
Lorvane Botanicâ„¢

Reason: I did a vote, No one is very excited about the current designs Im not sure what to do next

Target Market(s)

Designed for pet owners and pet grooming professionals.

Industry/Entity Type

Pet Care

Requirements
Must have
• - The label should have a common language between products; same them, that can be modified to all products by change of writing and picture.
• - Reflects the natural aspect of the company & products, safe for the children and pets, was NOT tested on animals
• - Unique feature of the product (one destined for male dogs, other for female, the third for cats)
• Attached company Logo (Lorvane Botanicâ„¢); should appear on the label.
• - Emphasize the difference for male / female dogs.
Nice to have
• - Maybe cartoon of a family bathing the male dog / female dog / cat - ?
• I think that the common feature should be a cartoon of a pet owner/s with different pets
• Made in the USA
• - Bottles are white
• - Dimensions:
• Male dog / Female dog / Odor & stain - 6"x7" & 4.25"x11"
• Cat: 4.5"x2.5" front & back
Should not have
• Please don't use stock images;
• We do private label and cannot have similar photos as our customers, must be unique.

```html
<!DOCTYPE html>
<html lang="en">
<head>
<meta charset="utf-8">
<title>Lorvane Botanic Oatmeal Pet Shampoo Labels</title>
<link rel="stylesheet" href="https://fonts.googleapis.com/css2?family=Montserrat:wght@400;800;900&family=Open+Sans:wght@400;600;700&family=Passion+One:wght@700&display=swap">
<style>
  :root {
    --page: #f7f7f7;
    --card: #ffffff;
    --blue-dark: #174a94;
    --blue-mid: #2c7be0;
    --blue-light: #cfe4fb;
    --pink-dark: #b02e6c;
    --pink-mid: #c94d8c;
    --pink-light: #eaa7c9;
    --green-light: #d7f0c4;
    --green-mid: #9fdb72;
    --green-deep: #5ab52a;
    --grey-logo: #7a7a7a;
  }
  * { margin: 0; padding: 0; box-sizing: border-box; }
  html, body { width: 1200px; height: 859px; overflow: hidden; background: var(--page); }
  body { position: relative; font-family: "Open Sans", Arial, sans-serif; }

  .label-card {
    position: absolute; top: 156px; width: 387px; height: 573px;
    background: var(--card);
    box-shadow: 0 1px 4px rgba(0,0,0,.35);
  }
  .label-card--male { left: 169px; }
  .label-card--female { left: 659px; }

  .label-art { position: absolute; left: 8px; top: 12px; width: 368px; height: 548px; overflow: hidden; }
  .label-art svg.label-bg { position: absolute; inset: 0; }

  .line { position: absolute; left: 0; width: 100%; text-align: center; white-space: nowrap; }

  .brand {
    top: 18px; font-family: "Montserrat", sans-serif; font-weight: 400;
    font-size: 19px; color: var(--grey-logo); letter-spacing: .5px;
    display: flex; justify-content: center; align-items: center; gap: 7px;
  }
  .brand-dot { width: 12px; height: 12px; border-radius: 50%; background: var(--green-deep); }

  .pet-name {
    font-family: "Passion One", sans-serif; font-weight: 700; line-height: .9;
  }
  .label-card--male .pet-name { top: 190px; font-size: 62px; color: var(--blue-light); -webkit-text-stroke: 1.5px var(--blue-dark); }
  .label-card--female .pet-name { top: 205px; font-size: 52px; color: var(--pink-dark); -webkit-text-stroke: 1px #fff; }

  .scent-pill {
    position: absolute; left: 50%; transform: translateX(-50%);
    padding: 1px 10px; border-radius: 10px;
    font-family: "Open Sans", sans-serif; font-weight: 600; font-size: 12px;
    letter-spacing: .6px; color: #fff; white-space: nowrap;
  }
  .label-card--male .scent-pill { top: 279px; background: var(--blue-dark); color: var(--blue-light); }
  .label-card--female .scent-pill { top: 480px; background: var(--pink-dark); }

  .product-title {
    font-family: "Montserrat", sans-serif; font-weight: 900; line-height: 1;
    -webkit-text-stroke: 2px #fff; paint-order: stroke fill;
  }
  .product-title--oat { font-size: 41px; }
  .product-title--shampoo { font-size: 43px; }
  .label-card--male .product-title { color: var(--blue-dark); }
  .label-card--female .product-title { color: var(--pink-dark); }
  .label-card--male .product-title--oat { top: 310px; }
  .label-card--male .product-title--shampoo { top: 351px; }
  .label-card--female .product-title--oat { top: 324px; }
  .label-card--female .product-title--shampoo { top: 365px; }

  .claims { font-weight: 700; font-size: 13px; line-height: 15px; letter-spacing: -.2px; }
  .label-card--male .claims { top: 413px; color: var(--blue-dark); }
  .label-card--female .claims { top: 421px; color: var(--pink-dark); }

  .ingredients { font-size: 14px; font-weight: 400; }
  .label-card--male .ingredients { top: 471px; color: var(--blue-dark); }
  .label-card--female .ingredients { top: 460px; color: var(--pink-dark); }

  .net-contents { font-weight: 700; font-size: 14px; letter-spacing: -.2px; }
  .label-card--male .net-contents { top: 515px; color: var(--blue-dark); }
  .label-card--female .net-contents { top: 514px; color: var(--pink-dark); }
</style>
</head>
<body>

<!-- Male dog label -->
<section class="label-card label-card--male">
  <div class="label-art">
    <svg class="label-bg" width="368" height="548" viewBox="0 0 368 548">
      <defs>
        <linearGradient id="male-green" x1="0" y1="0" x2="1" y2="1">
          <stop offset="0" stop-color="#eaf7df"/>
          <stop offset=".6" stop-color="#b4e28e"/>
          <stop offset="1" stop-color="#7cc94a"/>
        </linearGradient>
        <linearGradient id="male-swoosh" x1="0" y1="0" x2=".4" y2="1">
          <stop offset="0" stop-color="#2a7be0"/>
          <stop offset=".45" stop-color="#4c95ea"/>
          <stop offset=".75" stop-color="#ffffff"/>
          <stop offset="1" stop-color="#ffffff"/>
        </linearGradient>
        <linearGradient id="male-frame-fill" x1="0" y1="0" x2="0" y2="1">
          <stop offset="0" stop-color="#dff2cf"/>
          <stop offset=".45" stop-color="#8fb9c6"/>
          <stop offset="1" stop-color="#1f5fb3"/>
        </linearGradient>
        <radialGradient id="male-pet" cx=".5" cy=".45" r=".55">
          <stop offset="0" stop-color="#e8c48a"/>
          <stop offset=".7" stop-color="#c99a5a"/>
          <stop offset="1" stop-color="#c99a5a" stop-opacity="0"/>
        </radialGradient>
      </defs>
      <rect width="368" height="548" fill="url(#male-green)"/>
      <path d="M0 0 H40 C120 80 170 200 200 300 C230 400 270 480 330 548 H0 Z" fill="url(#male-swoosh)"/>
      <path d="M40 70 C40 55 60 48 90 48 C150 40 230 40 290 48 C330 52 340 70 340 100 L340 270 L290 265 L40 218 Z" fill="var(--blue-dark)"/>
      <path d="M48 78 C48 62 66 56 92 56 C150 50 228 50 286 56 C318 60 328 72 328 98 L326 258 L48 208 Z" fill="url(#male-frame-fill)"/>
      <ellipse cx="184" cy="126" rx="105" ry="88" fill="url(#male-pet)" role="img" aria-label="Illustration of a smiling golden retriever puppy resting its paws on the name badge"/>
      <ellipse cx="181" cy="228" rx="138" ry="36" fill="#ffffff"/>
      <ellipse cx="181" cy="226" rx="133" ry="32" fill="var(--blue-mid)" stroke="var(--blue-dark)" stroke-width="3"/>
      <circle cx="30" cy="262" r="14" fill="#ffffff" opacity=".55" role="img" aria-label="Paw print mark"/>
      <circle cx="335" cy="455" r="22" fill="#ffffff" opacity=".8" role="img" aria-label="Paw print mark"/>
      <rect x="0" y="533" width="368" height="15" fill="var(--blue-dark)"/>
    </svg>
    <div class="line brand"><span class="brand-dot"></span>Lorvane Botanic</div>
    <div class="line pet-name">Pippin</div>
    <div class="scent-pill">SPECIALLY SCENTED FOR MALE DOGS</div>
    <div class="line product-title product-title--oat">OATMEAL</div>
    <div class="line product-title product-title--shampoo">PET SHAMPOO</div>
    <div class="line claims">Deodorizing, PH Balanced, Pure and Natural<br>Super Concentrated</div>
    <div class="line ingredients">ALOE VERA · CHAMOMILE · VITAMIN E</div>
    <div class="line net-contents">Net Contents 16 FL. OZ. (472 ML)</div>
  </div>
</section>

<!-- Female dog label -->
<section class="label-card label-card--female">
  <div class="label-art">
    <svg class="label-bg" width="368" height="548" viewBox="0 0 368 548">
      <defs>
        <linearGradient id="female-green" x1="0" y1="0" x2="1" y2="1">
          <stop offset="0" stop-color="#eaf7df"/>
          <stop offset=".6" stop-color="#b4e28e"/>
          <stop offset="1" stop-color="#5ab52a"/>
        </linearGradient>
        <linearGradient id="female-swoosh" x1="0" y1="0" x2=".4" y2="1">
          <stop offset="0" stop-color="#b8316f"/>
          <stop offset=".45" stop-color="#cf5a93"/>
          <stop offset=".75" stop-color="#ffffff"/>
          <stop offset="1" stop-color="#ffffff"/>
        </linearGradient>
        <linearGradient id="female-frame-fill" x1="0" y1="0" x2="0" y2="1">
          <stop offset="0" stop-color="#dff2cf"/>
          <stop offset=".5" stop-color="#d88db0"/>
          <stop offset="1" stop-color="#b8316f"/>
        </linearGradient>
        <radialGradient id="female-pet" cx=".5" cy=".45" r=".55">
          <stop offset="0" stop-color="#dcae86"/>
          <stop offset=".7" stop-color="#b9875f"/>
          <stop offset="1" stop-color="#b9875f" stop-opacity="0"/>
        </radialGradient>
      </defs>
      <rect width="368" height="548" fill="url(#female-green)"/>
      <path d="M0 0 H40 C120 80 170 200 200 300 C230 400 270 480 330 548 H0 Z" fill="url(#female-swoosh)"/>
      <path d="M30 80 C30 60 50 52 80 52 C150 44 240 44 300 52 C330 56 340 72 340 100 L340 280 L300 276 L30 230 Z" fill="var(--pink-dark)"/>
      <path d="M38 86 C38 68 56 60 82 60 C150 54 236 54 294 60 C320 64 330 76 330 100 L328 266 L38 218 Z" fill="url(#female-frame-fill)"/>
      <ellipse cx="190" cy="135" rx="115" ry="100" fill="url(#female-pet)" role="img" aria-label="Illustration of a groomed apricot poodle standing in profile"/>
      <ellipse cx="177" cy="258" rx="137" ry="57" fill="var(--pink-dark)"/>
      <ellipse cx="177" cy="251" rx="136" ry="54" fill="var(--pink-light)" stroke="#ffffff" stroke-width="2"/>
      <circle cx="30" cy="316" r="16" fill="#ffffff" opacity=".55" role="img" aria-label="Paw print mark"/>
      <circle cx="338" cy="428" r="22" fill="#ffffff" opacity=".8" role="img" aria-label="Paw print mark"/>
      <rect x="0" y="533" width="368" height="15" fill="var(--pink-dark)"/>
    </svg>
    <div class="line brand"><span class="brand-dot"></span>Lorvane Botanic</div>
    <div class="line pet-name">Velvet<br>furry</div>
    <div class="line product-title product-title--oat">OATMEAL</div>
    <div class="line product-title product-title--shampoo">PET SHAMPOO</div>
    <div class="line claims">Deodorizing, PH Balanced, Pure and Natural<br>Super Concentrated</div>
    <div class="line ingredients">ALOE VERA · CHAMOMILE · VITAMIN E</div>
    <div class="scent-pill">SPECIALLY SCENTED FOR FEMALE DOGS</div>
    <div class="line net-contents">Net Contents 16 FL. OZ. (472 ML)</div>
  </div>
</section>

</body>
</html>
```